Flexora Workout Grips

We are looking for a postcard to include in our marketing platform. We will place this postcard in an envelope along with our product and send it to various gyms around the country. The product is called "Flexora". Flexora are unique rubber workout grips that men and women use to lift weights, reducing the stress on their hands and eliminating those painful calluses. www.Flexora.example. We want to highlight the logo in the front of the postcard, along with our web ad. The back of the card should have the wholesale purchasing information which is as follows: 1(one) box of workout grips with 20 (twenty) pairs at a wholesale price of $5 per pair. It should also include our e-mail address, flexorafitnessllc@mailbox.example along with our telephone numbers Ned (555)-214-0637 and Oren (555)-480-1792

Reason: I've only seen two designs so far so I wanted to extend the time for everyone to submit their designs. Hope this helps. Ned

```html
<!DOCTYPE html>
<html lang="en">
<head>
<meta charset="utf-8">
<title>Flexora Workout Grips – Wholesale Postcard</title>
<link rel="stylesheet" href="https://fonts.googleapis.com/css2?family=Open+Sans:wght@400;600&display=swap">
<style>
  :root {
    --card-black: #141415;
    --swoosh-grey: #4d4a47;
    --brand-red: #d0222a;
    --brand-green: #149a46;
    --text-white: #ffffff;
  }
  html, body {
    margin: 0;
    padding: 0;
    overflow: hidden;
    background: var(--card-black);
  }
  .postcard {
    position: relative;
    width: 1200px;
    height: 929px;
    background: var(--card-black);
    overflow: hidden;
    font-family: "Open Sans", sans-serif;
    color: var(--text-white);
  }
  .backdrop {
    position: absolute;
    inset: 0;
    width: 1200px;
    height: 929px;
  }
  .contact {
    position: absolute;
    right: 255px;
    top: 64px;
    margin: 0;
    text-align: right;
    font-size: 33px;
    line-height: 48px;
    letter-spacing: 4.5px;
    font-style: normal;
  }
  .contact span { display: block; }
  .brand {
    position: absolute;
    left: 965px;
    top: 104px;
    display: flex;
    align-items: center;
    gap: 10px;
    color: var(--brand-red);
    font-size: 38px;
    font-weight: 600;
    letter-spacing: 1px;
  }
  .brand-square {
    width: 22px;
    height: 22px;
    background: var(--brand-red);
  }
  .offer {
    position: absolute;
    left: 0;
    width: 1210px;
    top: 326px;
    margin: 0;
    text-align: center;
    font-size: 66px;
    font-weight: 400;
    line-height: 82.5px;
    letter-spacing: 5.5px;
    text-transform: uppercase;
  }
</style>
</head>
<body>
  <main class="postcard">
    <svg class="backdrop" viewBox="0 0 1200 929" aria-hidden="true">
      <defs>
        <linearGradient id="swoosh-fade" x1="0" y1="0" x2="1" y2="0">
          <stop offset="0" stop-color="var(--swoosh-grey)" stop-opacity="1"/>
          <stop offset="0.45" stop-color="var(--swoosh-grey)" stop-opacity="0.55"/>
          <stop offset="1" stop-color="var(--swoosh-grey)" stop-opacity="0.25"/>
        </linearGradient>
      </defs>
      <path class="swoosh" fill="url(#swoosh-fade)"
        d="M1200 152 C620 168 0 290 0 500 C0 650 250 810 500 912
           C290 800 168 660 175 545 C185 330 620 228 1200 212 Z"/>
      <polygon class="accent-red" fill="var(--brand-red)"
        points="760,800 852,712 1200,712 1200,929 905,929"/>
      <polygon class="accent-green" fill="var(--brand-green)"
        points="470,929 712,784 978,858 1042,929"/>
    </svg>

    <address class="contact">
      <span class="contact-email">flexorafitnessllc@mailbox.example</span>
      <span class="contact-phone">Ned (555)-214-0637</span>
      <span class="contact-phone">Oren (555)-480-1792</span>
    </address>

    <div class="brand">
      <span class="brand-square"></span>
      <span class="brand-name">Flexora</span>
    </div>

    <h1 class="offer">1 box of workout<br>grips with 20 pairs<br>at a wholesale<br>price of $5 per pair</h1>
  </main>
</body>
</html>
```